Weight loss surgery restaurant card

We need to create a card for patients who have undergone weight loss surgery to take to restaurants so they can request smaller meals. These patients have had surgery on their stomach so that they can only consume half to one cup of food at a time. So normal sized restaurant meals are way too big (and cost a lot). This card they can present to the restaurant to communicate the fact that they have had weight loss surgery and therefore request a smaller meal portion at reduced cost

Target Market(s)

Restaurants serving weight loss surgery patients

Industry/Entity Type

Health Care

Contact Information for Business Card

This will be a plastic card similar to business card size.

Requirements
Must have
• The front of the card should include the following text:
• The individual bearing this card has undergone weight loss surgery.
• This surgery restricts portion sizes to between half and one cup of food at a time.
• Please give consideration to allowing smaller portions of your regular meals to be ordered to reduce wastage and excess costs.
• Example: a half size portion priced at two thirds of usual cost.
• The back of the card will have spaces for the person to write certain information. These are the categories that can be filled in by hand:
• Name:
• Procedure performed:
• Date of procedure (month/year):
• Treating Clinic Name:
• Treating Clinic Signature:
• Somewhere down the bottom should be something along the lines of:
• supplied from bernardwhitlow.com.au
Nice to have
• A nice design with imagery/colours etc ... not just the text on a white background! Bright attractive colours preferred.
• I have uploaded my logo ... a roughly triangular image followed by my name etc. The triangular logo image could be used somewhere on the card and this logo can be interchangeable for other clinics who purchase the card.
• **Please note that I don't want my name to be included as part of the logo on the card ... just use the triangular image on the side of the logo without the following name**
• Also, the colouring of the card does not have to reflect my logo colours as I am anticipating interchanging this logo with other logos if other clinics choose to adopt the card. I am interested to see other, more generic, colour choices as well as my logo colours

```html
<!DOCTYPE html>
<html lang="en">
<head>
<meta charset="utf-8">
<title>Weight Loss Surgery Restaurant Card</title>
<link href="https://fonts.googleapis.com/css2?family=Lato:wght@400;700&display=swap" rel="stylesheet">
<style>
  :root {
    --stage: #2b2b2b;
    --paper: #ffffff;
    --ink: #1f1f1f;
    --navy-blue: #0f57b0;
    --deep-blue: #1a5fb4;
    --sky-blue: #49b8ea;
    --accent-orange: #f26b1d;
    --brand-teal: #1f9c8e;
    --divider: #555555;
  }
  * { box-sizing: border-box; margin: 0; padding: 0; }
  html, body { width: 1200px; height: 900px; overflow: hidden; }
  body {
    background: var(--stage);
    font-family: "Lato", Arial, sans-serif;
    color: var(--ink);
    position: relative;
  }
  .card {
    position: absolute;
    width: 560px;
    height: 320px;
    background: var(--paper);
    border-radius: 4px;
    overflow: hidden;
  }
  /* Back of card: fill-in fields */
  .card-back { left: 60px; top: 70px; }
  .brand-mark {
    display: flex; align-items: center; gap: 8px;
    font-size: 17px; font-weight: 700; color: var(--brand-teal);
  }
  .brand-mark .dot {
    width: 14px; height: 14px; border-radius: 50%; background: var(--brand-teal);
  }
  .card-back .brand-mark { position: absolute; right: 40px; top: 38px; }
  .field-list {
    position: absolute; left: 48px; top: 120px;
    list-style: none; font-size: 15px; line-height: 27px;
  }
  .field-list li { letter-spacing: 0.2px; }
  .supplied-band {
    position: absolute; left: 0; right: 0; bottom: 0; height: 48px;
    background: var(--navy-blue); color: var(--paper);
    display: flex; align-items: center; justify-content: center;
    font-size: 15px; letter-spacing: 0.6px;
  }
  .supplied-band .domain-name { color: var(--accent-orange); }

  /* Front of card: message */
  .card-front { left: 580px; top: 510px; }
  .front-header {
    position: absolute; left: 0; right: 0; top: 0; height: 160px;
    display: flex; align-items: center; justify-content: center; gap: 26px;
  }
  .header-divider { width: 1px; height: 80px; background: var(--divider); }
  .contact-list { list-style: none; font-size: 14px; line-height: 25px; }
  .contact-list li { display: flex; align-items: center; gap: 8px; }
  .contact-list svg { width: 12px; height: 12px; fill: var(--deep-blue); flex: none; }
  .message-panel {
    position: absolute; left: 0; right: 0; bottom: 0; height: 160px;
    background: linear-gradient(90deg, var(--deep-blue) 0%, #2a8fd6 55%, var(--sky-blue) 100%);
    color: var(--paper);
    display: grid; grid-template-columns: 1fr 1fr; gap: 22px;
    padding: 22px 26px 18px;
  }
  .message-column { list-style: none; font-size: 12.5px; line-height: 17px; }
  .message-column li { position: relative; padding-left: 16px; margin-bottom: 12px; }
  .message-column li::before {
    content: ""; position: absolute; left: 0; top: 5px;
    width: 7px; height: 7px; border-radius: 50%; background: var(--accent-orange);
  }
</style>
</head>
<body>

<section class="card card-back">
  <div class="brand-mark"><span class="dot"></span>Whitlow Clinic</div>
  <ul class="field-list">
    <li>Name:</li>
    <li>Procedure performed:</li>
    <li>Date of procedure (month/year):</li>
    <li>Treating Clinic Name:</li>
    <li>Treating Clinic Signature:</li>
  </ul>
  <div class="supplied-band">Supplied from&nbsp;www.<span class="domain-name">bernardwhitlow</span>.com.au</div>
</section>

<section class="card card-front">
  <div class="front-header">
    <div class="brand-mark"><span class="dot"></span>Whitlow Clinic</div>
    <div class="header-divider"></div>
    <ul class="contact-list">
      <li><svg viewBox="0 0 24 24"><path d="M6.6 10.8a15 15 0 0 0 6.6 6.6l2.2-2.2a1 1 0 0 1 1-.25 11.4 11.4 0 0 0 3.6.57 1 1 0 0 1 1 1V20a1 1 0 0 1-1 1A17 17 0 0 1 3 4a1 1 0 0 1 1-1h3.5a1 1 0 0 1 1 1c0 1.25.2 2.45.57 3.57a1 1 0 0 1-.25 1z"/></svg>(03) 9421 6083</li>
      <li><svg viewBox="0 0 24 24"><path d="M2 5h20v14H2z M2 5l10 8 10-8" /></svg>info@bernardwhitlow.com.au</li>
      <li><svg viewBox="0 0 24 24"><path d="M12 2a10 10 0 1 0 0 20 10 10 0 0 0 0-20zm0 2c1.2 1.4 2 3.6 2.2 7H9.8C10 7.6 10.8 5.4 12 4zm-2.2 9h4.4c-.2 3.4-1 5.6-2.2 7-1.2-1.4-2-3.6-2.2-7zM4.1 11a8 8 0 0 1 4.6-6.3C8.1 6.4 7.8 8.6 7.8 11zm0 2h3.7c0 2.4.3 4.6.9 6.3A8 8 0 0 1 4.1 13zm12.1 0h3.7a8 8 0 0 1-4.6 6.3c.6-1.7.9-3.9.9-6.3zm0-2c0-2.4-.3-4.6-.9-6.3a8 8 0 0 1 4.6 6.3z"/></svg>www.bernardwhitlow.com.au</li>
    </ul>
  </div>
  <div class="message-panel">
    <ul class="message-column">
      <li>The individual bearing this card has undergone weight loss surgery.</li>
      <li>Please give consideration to allowing smaller portions of your regular meals to be ordered to reduce wastage and excess costs.</li>
    </ul>
    <ul class="message-column">
      <li>This surgery restricts portion sizes to between half and one cup of food at a time.</li>
      <li>Example: a half size portion priced at two thirds of usual cost.</li>
    </ul>
  </div>
</section>

</body>
</html>
```